Home inspection business! professional look attracting customers just by looks. Read must haves

its a new business I started on my own for home inspections I would like something very professional to give to real estate agents and clients, its going to have my license number on it my business phone number my name my website as well etc on the back side it will be servicing areas and also what kind of services I offer I also have a business card from someone else the way I would like mine to be. I will attach my logo

Industry/Entity Type

Home Inspection

Contact Information for Business Card

listed in nice to haves

Requirements
Must have
• phone number - 718 352 9047
• website- crestwoodlatch.example
• license number #2749035186
• my name Gavin teraskovic
• picture of my logo and me on the front
• on the back of the card. stating I am servicing All of New York and Long Island
• also services I will offer will be home inspection -mold inspection -lead inspection -radon inspection -Termite Inspection -Infared Scan.
• and also we provide inspections for single family homes condos co-ops town-homes
• and commercial property
Nice to have
• same colors as the logos and also if you recommend fonts to look like the logo not sure up to you

```html
<!DOCTYPE html>
<html lang="en">
<head>
<meta charset="utf-8">
<title>Crestwood Latch – Business Card</title>
<link rel="stylesheet" href="https://fonts.googleapis.com/css2?family=Poppins:wght@400;500;600&display=swap">
<style>
  :root {
    --backdrop: #e4dccf;
    --card-white: #ffffff;
    --card-grey: #737373;
    --brand-blue: #4a9ad6;
    --ink-dark: #4a4a4a;
    --ink-light: #ffffff;
    --logo-grey: #6f6f6f;
  }
  * { box-sizing: border-box; margin: 0; padding: 0; }
  html, body {
    width: 1200px; height: 900px; overflow: hidden;
    background: var(--backdrop);
    font-family: "Poppins", sans-serif;
  }
  .canvas { position: relative; width: 1200px; height: 900px; }

  .card {
    position: absolute; left: 311px; width: 577px; height: 329px;
    box-shadow: 0 6px 14px rgba(0,0,0,0.22);
    overflow: hidden;
  }

  /* Back side */
  .card-back { top: 98px; background: var(--card-grey); color: var(--ink-light); }
  .card-back .brand {
    position: absolute; left: 32px; top: 140px;
    display: flex; align-items: center; gap: 10px;
  }
  .brand-dot { width: 18px; height: 18px; border-radius: 50%; background: var(--brand-blue); }
  .brand-name {
    font-size: 24px; font-weight: 600; letter-spacing: 0.5px;
    text-transform: uppercase; white-space: nowrap;
  }
  .card-back .brand-name { color: var(--ink-light); }

  .service-area {
    position: absolute; left: 307px; top: 48px;
    font-size: 13.5px; font-weight: 500; color: var(--brand-blue);
    letter-spacing: 0.2px;
  }
  .property-types {
    position: absolute; left: 307px; top: 85px;
    font-size: 14.5px; line-height: 21px; font-weight: 500;
  }
  .service-list {
    position: absolute; left: 307px; top: 163px;
    list-style: none; font-size: 14px; line-height: 20.6px;
    font-weight: 500; letter-spacing: 0.6px;
  }
  .service-list li::before { content: "•"; margin-right: 7px; }

  /* Front side */
  .card-front { top: 472px; background: var(--card-white); color: var(--ink-dark); }
  .portrait {
    position: absolute; left: 52px; top: 31px; width: 124px; height: 124px;
    border-radius: 50%;
    background: radial-gradient(circle at 50% 35%, #c9b6a4 0%, #6a7a92 55%, #d8dde2 100%);
  }
  .card-front .brand { position: absolute; left: 296px; top: 76px; display: flex; align-items: center; gap: 10px; }
  .card-front .brand-name { color: var(--logo-grey); font-size: 23px; }
  .card-front .brand-dot { background: var(--brand-blue); }

  .holder { position: absolute; left: 32px; top: 177px; }
  .holder-name {
    font-size: 15px; font-weight: 500; color: var(--brand-blue);
    text-transform: uppercase; letter-spacing: 0.3px;
  }
  .holder-license { font-size: 13.5px; color: var(--ink-dark); margin-top: 1px; }

  .divider {
    position: absolute; left: 32px; top: 228px; width: 514px; height: 2px;
    background: var(--brand-blue);
  }
  .contact-list {
    position: absolute; left: 32px; top: 245px; list-style: none;
    font-size: 14px; color: var(--ink-dark);
  }
  .contact-list li { display: flex; align-items: center; gap: 9px; height: 23px; }
  .contact-list svg { width: 16px; height: 16px; fill: var(--brand-blue); }
  .base-band {
    position: absolute; left: 0; bottom: 0; width: 100%; height: 12px;
    background: var(--brand-blue);
  }
</style>
</head>
<body>
<main class="canvas">

  <section class="card card-back" aria-label="Card back">
    <div class="brand">
      <span class="brand-dot"></span>
      <span class="brand-name">Crestwood Latch</span>
    </div>
    <p class="service-area">ALL OF NEW YORK &amp; LONG ISLAND</p>
    <p class="property-types">Single Family Homes, Condos<br>Co-Ops Town-Homes &amp;<br>Commercia Property</p>
    <ul class="service-list">
      <li>HOME INSPECTION</li>
      <li>MOLD INSPECTION</li>
      <li>LEAD INSPECTION</li>
      <li>RADON INSPECTION</li>
      <li>TERMITE INSPECTION</li>
      <li>INFARED SCAN</li>
    </ul>
  </section>

  <section class="card card-front" aria-label="Card front">
    <div class="portrait" role="img" aria-label="Portrait photo of the inspector"></div>
    <div class="brand">
      <span class="brand-dot"></span>
      <span class="brand-name">Crestwood Latch</span>
    </div>
    <div class="holder">
      <p class="holder-name">Gavin Teraskovic</p>
      <p class="holder-license">LIC NO : #2749035186</p>
    </div>
    <div class="divider"></div>
    <ul class="contact-list">
      <li>
        <svg viewBox="0 0 24 24" aria-hidden="true"><path d="M6.6 10.8a15.1 15.1 0 0 0 6.6 6.6l2.2-2.2a1 1 0 0 1 1-.25 11.4 11.4 0 0 0 3.6.57 1 1 0 0 1 1 1V20a1 1 0 0 1-1 1A17 17 0 0 1 3 4a1 1 0 0 1 1-1h3.5a1 1 0 0 1 1 1c0 1.25.2 2.45.57 3.57a1 1 0 0 1-.25 1z"/></svg>
        <span>718 352 9047</span>
      </li>
      <li>
        <svg viewBox="0 0 24 24" aria-hidden="true"><path d="M12 2a10 10 0 1 0 0 20 10 10 0 0 0 0-20zm6.9 6h-2.9a15.6 15.6 0 0 0-1.4-3.6A8 8 0 0 1 18.9 8zM12 4c.8 1.2 1.5 2.5 1.9 4h-3.8c.4-1.5 1.1-2.8 1.9-4zM4.3 14a8 8 0 0 1 0-4h3.4a16.5 16.5 0 0 0 0 4zm.8 2h2.9c.3 1.3.8 2.5 1.4 3.6A8 8 0 0 1 5.1 16zM8 8H5.1a8 8 0 0 1 4.3-3.6C8.8 5.5 8.3 6.7 8 8zm4 12c-.8-1.2-1.5-2.5-1.9-4h3.8c-.4 1.5-1.1 2.8-1.9 4zm2.3-6H9.7a14.7 14.7 0 0 1 0-4h4.6a14.7 14.7 0 0 1 0 4zm.3 5.6c.6-1.1 1.1-2.3 1.4-3.6h2.9a8 8 0 0 1-4.3 3.6zm1.7-5.6a16.5 16.5 0 0 0 0-4h3.4a8 8 0 0 1 0 4z"/></svg>
        <span>www.crestwoodlatch.example</span>
      </li>
    </ul>
    <div class="base-band"></div>
  </section>

</main>
</body>
</html>
```